Legal Service Estimated Retainer and Average Case Value

We need an 11x14 flyer that contains the standard retainers and average cost be case, both provided in documents, for each case type we handle. We need the information displayed, preferably in a way that makes the information readable but less troubling to a client shocked at price of litigation. We need one sheet with the retainers and average case value merged into one table.

Target Market(s)

Potential Clients

Font styles to use
Serif
Sans Serif

```html
<!DOCTYPE html>
<html lang="en">
<head>
<meta charset="utf-8">
<title>Retainers and Average Case Costs</title>
<link href="https://fonts.googleapis.com/css2?family=Cinzel:wght@400;600&family=Arimo:wght@400;700&display=swap" rel="stylesheet">
<style>
  :root {
    --backdrop: #9a9a9a;
    --paper: #ffffff;
    --brand-blue: #1c4597;
    --head-gray: #8c8c8c;
    --row-gray: #dcdcdc;
    --rule: #9e9e9e;
    --ink: #111111;
    --frame: #2a2a2a;
    --photo-dark: #4a4440;
    --photo-mid: #9a9795;
    --photo-light: #c9c8c6;
  }
  * { box-sizing: border-box; margin: 0; padding: 0; }
  html, body { width: 1200px; height: 1200px; overflow: hidden; }
  body { background: var(--backdrop); font-family: "Arimo", Arial, sans-serif; color: var(--ink); }

  .flyer {
    position: absolute; left: 160px; top: 35px;
    width: 880px; height: 1130px;
    background: var(--paper);
    overflow: hidden;
  }
  .hero-photo {
    position: absolute; left: 0; top: 0; width: 100%; height: 280px;
    background: linear-gradient(110deg, var(--photo-dark) 0%, var(--photo-mid) 40%, var(--photo-light) 65%, var(--photo-mid) 85%, var(--photo-dark) 100%);
  }
  .firm-name {
    position: absolute; left: 70px; top: 100px;
    display: flex; align-items: center; gap: 18px;
    color: #fff; font-family: "Cinzel", Georgia, serif; font-weight: 400;
  }
  .firm-name .mark { width: 58px; height: 58px; border: 3px solid #fff; }
  .firm-name .lines { line-height: 1; }
  .firm-name .small { font-size: 16px; letter-spacing: 1px; }
  .firm-name .big { font-size: 40px; letter-spacing: 1px; }

  .accent-rule {
    position: absolute; left: 0; top: 270px; width: 100%; height: 14px;
    border-top: 8px solid var(--brand-blue);
  }
  .footer-band {
    position: absolute; left: 0; bottom: 0; width: 100%; height: 250px;
    background: var(--brand-blue);
  }
  .contact {
    position: absolute; left: 0; bottom: 40px; width: 100%;
    text-align: center; color: #fff; font-weight: 700;
  }
  .contact .consult { font-size: 34px; display: flex; justify-content: center; align-items: center; gap: 12px; }
  .contact .web { font-size: 28px; margin-top: 10px; }

  .rates-panel {
    position: absolute; left: 50px; top: 300px; width: 780px; height: 690px;
    background: var(--paper); border: 2px solid var(--frame);
    padding: 18px 22px;
  }
  .rates-title {
    font-family: "Cinzel", Georgia, serif; font-weight: 600;
    color: var(--brand-blue); font-size: 30px; text-align: center;
    letter-spacing: 0.5px; margin-bottom: 16px;
  }
  .tables { display: flex; gap: 16px; }
  .rate-table { flex: 1; border-collapse: collapse; table-layout: fixed; }
  .rate-table th {
    background: var(--head-gray); color: #fff; font-size: 20px; font-weight: 700;
    height: 40px; text-align: center;
  }
  .rate-table td {
    height: 44px; font-size: 13px; font-weight: 700; text-align: center;
    line-height: 1.15; padding: 0 6px;
  }
  .rate-table td + td, .rate-table th + th { border-left: 1px solid var(--rule); }
  .rate-table tbody tr:nth-child(even) td { background: var(--row-gray); }
  .rate-table .case-col { width: 54%; }
</style>
</head>
<body>
  <main class="flyer">
    <div class="hero-photo" role="img" aria-label="Photo of hands signing a legal document with a pen"></div>
    <div class="firm-name">
      <span class="mark"></span>
      <div class="lines">
        <div class="small">THE LAW OFFICE OF</div>
        <div class="big">MARIAN T WHITFIELD</div>
      </div>
    </div>
    <div class="accent-rule"></div>
    <div class="footer-band"></div>

    <section class="rates-panel">
      <h1 class="rates-title">RETAINERS AND AVERAGE CASE COSTS:</h1>
      <div class="tables">
        <table class="rate-table">
          <colgroup><col class="case-col"><col></colgroup>
          <thead><tr><th>Avarage Case</th><th>Cost</th></tr></thead>
          <tbody>
            <tr><td>(3301 C)</td><td>Retainer: $2,000</td></tr>
            <tr><td>(3301 D)</td><td>Retainer: $2,500</td></tr>
            <tr><td>Custody</td><td>Retainer: $3,500</td></tr>
            <tr><td>Equitable Distribution</td><td>Retainer: $3,500</td></tr>
            <tr><td>Support</td><td>Retainer: $3,000</td></tr>
            <tr><td>Custody and Support</td><td>Retainer: $3,500</td></tr>
            <tr><td>Equitable Distribution and Support</td><td>Retainer: $3,500</td></tr>
            <tr><td>Equitable Distribution and Custody</td><td>Retainer: $5,000</td></tr>
            <tr><td>Equitable Distribution, Custody and Support</td><td>Retainer: $3,500</td></tr>
            <tr><td>Custody Initial Order</td><td>Retainer: $3,000</td></tr>
            <tr><td>Custody Modification</td><td>Retainer: $3,500</td></tr>
            <tr><td>Custody and Support</td><td>Retainer: $3,000</td></tr>
            <tr><td>(PFA) Protection From Abuse</td><td>: $2,000 Paid In Full</td></tr>
          </tbody>
        </table>
        <table class="rate-table">
          <colgroup><col class="case-col"><col></colgroup>
          <thead><tr><th>Avarage Case</th><th>Cost</th></tr></thead>
          <tbody>
            <tr><td>Custody Contempt/Modification</td><td>$5,000 - $8,000</td></tr>
            <tr><td>Custody Initial Order</td><td>$4,000 - $7,000</td></tr>
            <tr><td>Custody &amp; Support</td><td>$5,000 - $8,000</td></tr>
            <tr><td>Support</td><td>$2,000 - $4,000</td></tr>
            <tr><td>Divorce (3301c)</td><td>$1,500 - $3,000</td></tr>
            <tr><td>Divorce (3301d)</td><td>$2,000 - $3,000</td></tr>
            <tr><td>Protection from Abuse</td><td>$1,500 - $3,000</td></tr>
            <tr><td>Divorce &amp; Custody</td><td>$5,000 - $8,000</td></tr>
            <tr><td>Divorce &amp; Equitable Distribution</td><td>$6,000 - $10,000</td></tr>
            <tr><td>Divorce, Custody &amp; Support</td><td>$8,000 - $12,000</td></tr>
            <tr><td>Divorce, Equitable Distribution &amp; Custody</td><td>$10,000 - $15,000</td></tr>
            <tr><td>Divorce, Equitable Distribution &amp; Support</td><td>$8,000 - $12,000</td></tr>
            <tr><td>Divorce, Equitable Distribution, Custody &amp; Support</td><td>$12,000 - $15,000</td></tr>
          </tbody>
        </table>
      </div>
    </section>

    <footer class="contact">
      <div class="consult">
        <span>Complimentary Consultations</span>
        <svg width="26" height="26" viewBox="0 0 24 24" aria-hidden="true"><rect x="1" y="1" width="22" height="22" rx="4" fill="#fff"/><path d="M8 5c1 0 1.5 2.5 1.5 3s-1.2 1-1 1.8c.5 2 2.7 4.2 4.7 4.7.8.2 1.3-1 1.8-1s3 .5 3 1.5-1.5 3-3 3C10 18 6 14 6 8.5 6 7 7 5 8 5z" fill="#1c4597"/></svg>
        <span>555.014.2290</span>
      </div>
      <div class="web">www.whitfieldfamilylaw.com</div>
    </footer>
  </main>
</body>
</html>
```